Business card design needed

Our modern electrical contracting company requires business card design utilising our logo and incorporating our tag line "Service when you need it". We specialise in assisting our customers 24/7 offering a breakdown service.

Industry/Entity Type

Electrical

Contact Information for Business Card

Marcus Penfold, Electrical contractor,Tel: (08) 8546 3071, Fax: (08) 8679 4305, Mob 0428 736 514, Email: marcus.penfold@brightwirepower.com.au, Web: www.brightwirepower.com.au

Requirements
Must have
• we require a 2 sided card.
Front- Logo, tag line and contact information.
Rear- service when you need it! Call now for our 24/7 breakdown service

```html
<!DOCTYPE html>
<html lang="en">
<head>
<meta charset="utf-8">
<title>Brightwire Power – Business Card</title>
<link href="https://fonts.googleapis.com/css2?family=Inter:wght@200;300;400;700&display=swap" rel="stylesheet">
<style>
  :root {
    --backdrop: #3a3d44;
    --card: #f7f7f5;
    --brand-blue: #3d55b8;
    --ink: #2a2a2c;
    --muted: #a3a3a6;
    --card-shadow: rgba(0, 0, 0, 0.35);
  }
  * { margin: 0; padding: 0; box-sizing: border-box; }
  html, body {
    width: 900px;
    height: 1200px;
    overflow: hidden;
    background: var(--backdrop);
    font-family: "Inter", "Helvetica Neue", Arial, sans-serif;
  }
  .sheet {
    width: 900px;
    height: 1200px;
    display: flex;
    flex-direction: column;
    align-items: center;
    justify-content: center;
    gap: 110px;
  }
  .card {
    position: relative;
    width: 700px;
    height: 400px;
    background: var(--card);
    box-shadow: 0 14px 30px var(--card-shadow);
    text-transform: uppercase;
  }

  /* Front */
  .brand {
    position: absolute;
    top: 40px;
    right: 44px;
    text-align: right;
  }
  .brand-row {
    display: flex;
    align-items: center;
    justify-content: flex-end;
    gap: 14px;
  }
  .brand-name {
    font-weight: 700;
    font-size: 30px;
    letter-spacing: 0.5px;
    color: var(--brand-blue);
  }
  .brand-dot {
    width: 46px;
    height: 46px;
    border-radius: 50%;
    background: var(--brand-blue);
  }
  .tagline {
    margin-top: 2px;
    font-weight: 300;
    font-size: 19px;
    color: var(--ink);
    letter-spacing: 0.3px;
  }
  .contact {
    position: absolute;
    left: 48px;
    top: 150px;
    font-weight: 300;
    line-height: 1.15;
  }
  .contact-name {
    font-size: 22px;
    color: var(--muted);
  }
  .contact-role {
    font-size: 22px;
    color: var(--brand-blue);
    margin-bottom: 8px;
  }
  .contact-line {
    font-size: 26px;
    color: var(--ink);
  }
  .contact-email {
    margin-top: 12px;
    font-size: 22px;
    color: var(--brand-blue);
  }

  /* Back */
  .back-message {
    position: absolute;
    left: 48px;
    bottom: 56px;
    display: flex;
    align-items: center;
    gap: 16px;
  }
  .call-badge {
    width: 74px;
    height: 62px;
    border-radius: 31px;
    background: var(--brand-blue);
    color: #fff;
    font-weight: 400;
    font-size: 15px;
    line-height: 1.05;
    display: flex;
    align-items: center;
    justify-content: center;
    text-align: center;
  }
  .back-lines { line-height: 1.1; font-weight: 300; }
  .back-tagline { font-size: 34px; color: var(--ink); }
  .back-service { font-size: 30px; color: var(--brand-blue); }
</style>
</head>
<body>
<main class="sheet">
  <section class="card card-front" aria-label="Business card front">
    <div class="brand">
      <div class="brand-row">
        <span class="brand-name">Brightwire Power</span>
        <span class="brand-dot" aria-hidden="true"></span>
      </div>
      <p class="tagline">Service when you need it</p>
    </div>
    <div class="contact">
      <p class="contact-name">Marcus Penfold</p>
      <p class="contact-role">Electrical contractor</p>
      <p class="contact-line">Tel (08) 8546 3071</p>
      <p class="contact-line">Fax (08) 8679 4305</p>
      <p class="contact-line">Mob 0428 736 514</p>
      <p class="contact-email">marcus.penfold@<br>brightwirepower.com.au</p>
    </div>
  </section>

  <section class="card card-back" aria-label="Business card back">
    <div class="back-message">
      <div class="call-badge">Call<br>now</div>
      <div class="back-lines">
        <p class="back-tagline">Service when you need it</p>
        <p class="back-service">For 24/7 breakdown service</p>
      </div>
    </div>
  </section>
</main>
</body>
</html>
```